MODERN + COOL Business Card Needed!

SUMMARY
This is for a 40+ year old family business that is transitioning to the 2nd generation and is in real need of a more modern facelift. Ive attached a company logo (I made quickly as an idea with my limited PSD skills) to start off with that you are welcome to change and draw ideas from. Ive also attached some screen shots of cards I like to give you an idea of my preferences.

WHAT WE DO
The company name is Tall Pine HK Ltd. But I prefer to just call it Tall Pine or Tall Pine with Hong Kong as kind of a sub heading on the business card. We own a factory as well as help our customers find factories to make their product. Product I mean, toys 99.9% of the time. Simple old school toys like board games, puzzles, wooden toys, baby/infant toys.

You can say we are a "sourcing" or "trading" or "consulting" company with a factory to help you do it. But since we deal with toys, i like to keep it modern and cool and fun, not serious like managing hedge funds.

WHAT WE ARE LOOKING FOR
A cool, unique looking business card that stands out. In terms of design, something modern and professional. I like darker colored cards and I like colors such as blue/green/dark gray, but am open to other colored themes. I Like bright lime green with gray, always though thats a nice combo. I prefer cards that are all colored and not so much white showing (I think). Ive attached a few screenshots of cards so take a look to get a feel of what I like.

We do alot of wooden stacking games in variety of colors too like Tovra, Lumo, Towerplix (google these to check them out). So designs that sort of resemble stacking or building would be cool but totally not necessary.

In terms of the physical aspects of the card, Im looking for a card a bit different than the standard rectangular shape. Double sided. Little things like having corner(s) be round or different angle instead of square edge I always thought was nice. Its got to be mostly a normal card size, no folding or smaller cards that fit weird in your wallet. No vertical designs. Am open to VERY different/creative shapes (as long as it still fits in a wallet good like a normal buisness card.
Updates

Hi everyone!

Just wanted to write a message to everyone to let them know all submissions are being reviewed or have been reviewed.  If I have not responded with feedback, rest assure your submission was definitely looked at in detail but I either have just been too busy to respond (alot of submissions!), or its on my to be considered list.

I respect and really enjoy receiving everyones creativity and work so I dont want it to go unrecognized - thus this message!  Feel free to submit more ideas if you like until this project ends.  Sometimes some designs just dont click but sometimes they can so you never know!

Thanks again for everyones participation and great work!

~Dev Orr

Target Market(s)

The cards are mainly handed to toy company sourcers and buyers. People I talk to ... say Pelvane for example... might want to make their next edition of Farthingale game with a reputable factory at a good cost so they can sell it to stores at a profit.

So these are the types of people I often try to talk and introduce myself and my company to.

Industry/Entity Type

Building

Colors
acd036
0392cd
00a88e
474747
606060

Requirements
Must have
• Just double sided, not plain rectangle corners, and just cool to look at and catches your eye!

Oh and the obvious business card stuff like place for name, address, number, email, etc.
Nice to have
• Think more modern and fun, not serious and old fashion (thats what we used to be!). Can use the logo I attached and you can definitely alter and change the logo or make a whole new one!

Oh and can definitely use a creative slogan if you like to think of one based on what I described in what we do.
Should not have
• Dont use fonts or text placement that might make "Tall Pine" look like "Tal Lpine"... We arent selling news papers!!

Please nothing related to education since we have the word Pine in the title, thats not our business at all.

Logo and design should not be too heavy on things related to toys, as though thats what we primarily focus on now, what we do may change over time.

```html
<!DOCTYPE html>
<html lang="en">
<head>
<meta charset="utf-8">
<title>Tall Pine HK Ltd. – Business Card</title>
<link rel="stylesheet" href="https://fonts.googleapis.com/css2?family=PT+Sans:ital,wght@0,400;0,700;1,400&display=swap">
<style>
  :root {
    --backdrop: #5e6e74;
    --card-white: #ffffff;
    --lime: #b6d77c;
    --lime-light: #cfe4a3;
    --lime-deep: #acd036;
    --ink: #2e2e2e;
    --ink-soft: #474747;
    --blue: #0392cd;
  }
  * { box-sizing: border-box; margin: 0; padding: 0; }
  html, body {
    width: 1200px;
    height: 960px;
    overflow: hidden;
  }
  body {
    background: var(--backdrop);
    font-family: "PT Sans", sans-serif;
    display: flex;
    flex-direction: column;
    align-items: center;
    justify-content: center;
    gap: 60px;
  }
  .card {
    position: relative;
    width: 630px;
    height: 360px;
    border-radius: 48px 0 48px 0;
    overflow: hidden;
    box-shadow: 0 12px 30px rgba(0, 0, 0, 0.3);
  }

  /* Front */
  .card--front { background: var(--card-white); }
  .card--front .details {
    position: absolute;
    left: 70px;
    top: 88px;
    right: 40px;
    color: var(--ink);
  }
  .person-name {
    font-size: 30px;
    font-weight: 400;
    line-height: 1.1;
  }
  .person-role {
    font-size: 24px;
    font-style: italic;
    margin-top: 2px;
  }
  .contact {
    display: grid;
    grid-template-columns: 1fr 1fr;
    column-gap: 24px;
    row-gap: 4px;
    margin-top: 16px;
    font-size: 17px;
    color: var(--ink-soft);
  }
  .contact-row:nth-child(1) { grid-column: 2; grid-row: 1; }
  .contact-row:nth-child(2) { grid-column: 1; grid-row: 2; }
  .contact-row:nth-child(3) { grid-column: 2; grid-row: 2; }
  .contact-row:nth-child(4) { grid-column: 1; grid-row: 3; }
  .card--front .brand-band {
    position: absolute;
    left: 0; right: 0; bottom: 0;
    height: 92px;
    background: var(--lime);
  }

  /* Brand lockup */
  .brand {
    position: absolute;
    display: flex;
    align-items: center;
    gap: 12px;
    color: var(--ink);
    font-weight: 700;
    line-height: 1;
  }
  .brand-dot {
    border-radius: 50%;
    background: var(--blue);
    flex: none;
  }
  .brand-name { display: block; }
  .brand-region { display: block; margin-top: 4px; }
  .card--front .brand { left: 70px; bottom: 18px; font-size: 24px; }
  .card--front .brand-dot { width: 40px; height: 40px; }

  /* Back */
  .card--back { background: var(--lime); }
  .card--back .lower-band {
    position: absolute;
    left: 0; right: 0; bottom: 0;
    height: 130px;
    background: var(--lime-light);
  }
  .card--back .brand { left: 60px; top: 150px; font-size: 40px; }
  .card--back .brand-dot { width: 64px; height: 64px; }
</style>
</head>
<body>

  <section class="card card--front" aria-label="Card front">
    <div class="details">
      <p class="person-name">Your Name</p>
      <p class="person-role">Position</p>
      <div class="contact">
        <p class="contact-row">Email: xxxxxxxxxxxxxxxxx</p>
        <p class="contact-row">Address: xxxxxxxxxxxxxxx</p>
        <p class="contact-row">Web: xxxxxxxxxxxxxxx xxx</p>
        <p class="contact-row">Phone: xxxxxxxxxxxxxxx</p>
      </div>
    </div>
    <div class="brand-band"></div>
    <div class="brand">
      <span class="brand-dot" aria-hidden="true"></span>
      <span>
        <span class="brand-name">tall pine ltd</span>
        <span class="brand-region">hong kong</span>
      </span>
    </div>
  </section>

  <section class="card card--back" aria-label="Card back">
    <div class="lower-band"></div>
    <div class="brand">
      <span class="brand-dot" aria-hidden="true"></span>
      <span>
        <span class="brand-name">tall pine ltd</span>
        <span class="brand-region">hong kong</span>
      </span>
    </div>
  </section>

</body>
</html>
```